Cosmetic injections clinic needs a fresh looking business card

We need a business card using the supplied logo and color scheme to attract future clients to our clinic. It should be modern and fresh, eye catching and not too busy. Simple and to the point is best. I would like two sided designs with the front indicating address and contact information, and the back in full color with white logo and descriptive information also provided.
Target Market(s)
Clients looking for non surgical beauty enhancements.
Contact Information for Business Card
Lumivela
14, 415 Carrow Ridge Road
St. Albert, Alberta
K2P 7W3
Phone: 431-662-0974
Email: info@lumivela-example.com
Requirements
Must have
- -Logo supplied with the name and address of the clinic
- -Back of card in full color with white logo with A small line of text indicating both of the following: Anti aging consultants and cosmetic injectables
- Located inside the Wayfarer Care Group

```html
<!DOCTYPE html>
<html lang="en">
<head>
<meta charset="utf-8">
<title>Lumivela Business Card</title>
<link rel="stylesheet" href="https://fonts.googleapis.com/css2?family=Roboto:wght@400;500;700&display=swap">
<style>
  :root {
    --backdrop: #2e2e30;
    --paper: #f2f2f2;
    --brand-purple: #6a4599;
    --brand-purple-deep: #5d3a8c;
    --brand-pink: #d9398b;
    --ink: #555555;
    --white: #ffffff;
  }
  * { margin: 0; padding: 0; box-sizing: border-box; }
  html, body {
    width: 1200px; height: 960px; overflow: hidden;
    background: var(--backdrop);
    font-family: "Roboto", Arial, sans-serif;
  }
  .canvas { position: relative; width: 1200px; height: 960px; }
  .card {
    position: absolute;
    width: 600px; height: 343px;
    border-radius: 22px;
    overflow: hidden;
  }
  .card--front { left: 302px; top: 124px; background: var(--paper); }
  .card--back { left: 299px; top: 493px; background: var(--brand-purple); }

  .front-art { position: absolute; left: 0; top: 0; width: 600px; height: 343px; }

  .contact-block { position: absolute; left: 48px; top: 82px; color: var(--ink); }
  .person-name {
    font-weight: 700; font-size: 19px; color: var(--brand-purple);
    letter-spacing: 0.2px; line-height: 22px;
  }
  .person-title {
    font-weight: 500; font-size: 15px; color: var(--brand-pink);
    line-height: 20px; margin-bottom: 8px;
  }
  .address { font-style: normal; font-size: 14.5px; line-height: 18.5px; margin-bottom: 8px; }
  .contact-list { list-style: none; font-size: 14.5px; line-height: 19.5px; }
  .contact-list li { display: flex; align-items: center; gap: 8px; }
  .contact-icon { width: 12px; height: 12px; fill: var(--brand-purple); flex: none; }

  .brand-name {
    position: absolute; left: 0; right: 0; top: 128px;
    text-align: center;
    font-weight: 500; font-size: 46px; letter-spacing: 2px;
    color: var(--white);
  }
  .tagline {
    position: absolute; left: 0; right: 0; top: 266px;
    text-align: center; color: var(--white);
    font-size: 14.5px; line-height: 18px;
  }
  .tagline-rule {
    width: 310px; height: 1px; margin: 5px auto 4px;
    background: var(--white);
  }
</style>
</head>
<body>
<main class="canvas">

  <section class="card card--front" aria-label="Business card front">
    <svg class="front-art" viewBox="0 0 600 343" role="img" aria-label="Brand illustration area: woman's profile with butterfly and flowing hair in purple, pink and teal">
      <defs>
        <linearGradient id="artFill" x1="0" y1="0" x2="1" y2="1">
          <stop offset="0" stop-color="var(--brand-purple)"/>
          <stop offset="1" stop-color="var(--brand-purple-deep)"/>
        </linearGradient>
      </defs>
      <circle cx="433" cy="172" r="135" fill="url(#artFill)"/>
      <path d="M438 0 H600 V343 H503 C560 280 560 150 520 60 C505 30 475 10 438 0 Z" fill="url(#artFill)"/>
    </svg>

    <div class="contact-block">
      <h1 class="person-name">DANIEL MOREAU</h1>
      <p class="person-title">CEO/FOUNDER</p>
      <address class="address">
        Lumivela<br>
        14, 415 Carrow Ridge Road<br>
        St. Albert, Alberta<br>
        K2P 7W3
      </address>
      <ul class="contact-list">
        <li>
          <svg class="contact-icon" viewBox="0 0 24 24" aria-hidden="true"><path d="M6.6 10.8a15.2 15.2 0 0 0 6.6 6.6l2.2-2.2c.3-.3.7-.4 1-.2 1.1.4 2.3.6 3.6.6.6 0 1 .4 1 1V20c0 .6-.4 1-1 1A17 17 0 0 1 3 4c0-.6.4-1 1-1h3.5c.6 0 1 .4 1 1 0 1.3.2 2.5.6 3.6.1.3 0 .7-.2 1L6.6 10.8Z"/></svg>
          431-662-0974
        </li>
        <li>
          <svg class="contact-icon" viewBox="0 0 24 24" aria-hidden="true"><path d="M2 5h20v14H2z M2 5l10 7 10-7" fill="var(--brand-purple)"/><path d="M3 6l9 6.3L21 6" fill="none" stroke="#f2f2f2" stroke-width="1.6"/></svg>
          info@lumivela-example.com
        </li>
        <li>
          <svg class="contact-icon" viewBox="0 0 24 24" aria-hidden="true"><circle cx="12" cy="12" r="10"/><path d="M2 12h20M12 2c3 3 3 17 0 20M12 2c-3 3-3 17 0 20" fill="none" stroke="#f2f2f2" stroke-width="1.4"/></svg>
          www.lumivela-example.com
        </li>
      </ul>
    </div>
  </section>

  <section class="card card--back" aria-label="Business card back">
    <p class="brand-name">LUMIVELA</p>
    <div class="tagline">
      <p>Anti aging consultants &amp; cosmetic injectables</p>
      <div class="tagline-rule"></div>
      <p>Located inside the Wayfarer Care Group</p>
    </div>
  </section>

</main>
</body>
</html>
```